MORLO's Coffee Liqueur Shot Arabica

Need a lable for a 500ml bottle of homemade Coffee liqueur.
Name:
MORLO's
Coffee
Shot

Shape: Round, 80mm
Color of the lable should be black and letters in black.
Letters MORLO's min 12mm hight.
Color of the liqueur is dark brown.
Add: 500ml
Add: 38% vol.
Should have a bean on the lable.
Maybe some bullet words on the bottom...
Prefered design see Pic1a with bottle.

Target Market(s)

People that enjoy coffee in shots, in coctails, with ice or on top of icecream or any other dessert

Font styles to use
Serif

Colors

Designer to choose colors to be used in the design.

Requirements
Must have
• See Pic 1a
Nice to have
• See Pic1a (bottle)
Should not have
• Different colors

```html
<!DOCTYPE html>
<html lang="en">
<head>
<meta charset="utf-8">
<title>MORLO's Coffee Shot – Label</title>
<link rel="stylesheet" href="https://fonts.googleapis.com/css2?family=Playfair+Display:wght@500;600;900&display=swap">
<style>
  :root {
    --paper: #f5f2ea;
    --label: #faf8f2;
    --ink: #1f231d;
    --gold: #c9a03a;
    --gold-deep: #a8801f;
  }
  html, body {
    margin: 0;
    padding: 0;
    width: 1200px;
    height: 1200px;
    overflow: hidden;
    background: var(--paper);
  }
  .label-canvas {
    display: block;
    width: 1200px;
    height: 1200px;
  }
  .label-disc { fill: var(--label); }
  .gold-rule { fill: none; stroke: var(--gold); }
  .brand-name,
  .product-name {
    font-family: "Playfair Display", Georgia, serif;
    font-weight: 900;
    fill: var(--ink);
  }
  .spec {
    font-family: "Playfair Display", Georgia, serif;
    font-weight: 500;
    font-size: 54px;
    fill: var(--ink);
  }
  .tagline {
    font-family: "Playfair Display", Georgia, serif;
    font-weight: 600;
    font-size: 60px;
    fill: var(--ink);
  }
  .ornament { fill: url(#ornamentTone); }
  .ornament-dot { fill: var(--gold); }
</style>
</head>
<body>
<svg class="label-canvas" viewBox="0 0 1200 1200" xmlns="http://www.w3.org/2000/svg">
  <defs>
    <radialGradient id="ornamentTone" cx="50%" cy="50%" r="50%">
      <stop offset="0%" stop-color="#c9a03a" stop-opacity="0.75"/>
      <stop offset="100%" stop-color="#c9a03a" stop-opacity="0.15"/>
    </radialGradient>
    <linearGradient id="beanTone" x1="0" y1="0" x2="1" y2="1">
      <stop offset="0%" stop-color="#8a6a26"/>
      <stop offset="55%" stop-color="#5a461c"/>
      <stop offset="100%" stop-color="#1f1b12"/>
    </linearGradient>
    <path id="taglineArc" d="M 270 872 Q 600 928 930 872"/>
  </defs>

  <!-- round label -->
  <circle class="label-disc" cx="600" cy="600" r="562"/>
  <circle class="gold-rule" cx="600" cy="600" r="552" stroke-width="5"/>
  <circle class="gold-rule" cx="600" cy="600" r="534" stroke-width="3"/>

  <!-- top flourish -->
  <rect class="ornament" x="370" y="132" width="460" height="88" rx="44" role="img" aria-label="Gold scrollwork flourish"/>

  <!-- brand name -->
  <text class="brand-name" x="600" y="368" text-anchor="middle" font-size="122" textLength="640" lengthAdjust="spacingAndGlyphs">MORLO'S</text>

  <!-- product banner -->
  <g class="product-banner">
    <rect class="gold-rule" x="172" y="404" width="856" height="184" rx="10" stroke-width="4"/>
    <rect class="gold-rule" x="192" y="424" width="816" height="144" rx="6" stroke-width="2.5"/>
    <circle class="ornament-dot" cx="150" cy="496" r="9"/>
    <circle class="ornament-dot" cx="1050" cy="496" r="9"/>
    <text class="product-name" x="600" y="534" text-anchor="middle" font-size="100" textLength="720" lengthAdjust="spacingAndGlyphs">COFFEE SHOT</text>
  </g>

  <!-- side flourishes under banner -->
  <rect class="ornament" x="190" y="606" width="220" height="76" rx="38" role="img" aria-label="Gold scrollwork flourish, left"/>
  <rect class="ornament" x="790" y="606" width="220" height="76" rx="38" role="img" aria-label="Gold scrollwork flourish, right"/>

  <!-- coffee bean -->
  <ellipse cx="588" cy="716" rx="110" ry="84" transform="rotate(-22 588 716)" fill="url(#beanTone)" role="img" aria-label="Engraved coffee bean in gold and black"/>

  <!-- specs -->
  <text class="spec" x="218" y="762">500 ml</text>
  <text class="spec" x="962" y="762" text-anchor="end">38% vol.</text>

  <!-- tagline ribbon -->
  <g class="tagline-ribbon">
    <path class="gold-rule" d="M 235 810 Q 600 858 965 810" stroke-width="4"/>
    <path class="gold-rule" d="M 250 920 Q 600 968 950 920" stroke-width="4"/>
    <path class="gold-rule" d="M 235 810 Q 215 865 250 920" stroke-width="4"/>
    <path class="gold-rule" d="M 965 810 Q 985 865 950 920" stroke-width="4"/>
    <text class="tagline"><textPath href="#taglineArc" startOffset="50%" text-anchor="middle">Arabica • Intense</textPath></text>
  </g>

  <!-- bottom flourish -->
  <rect class="ornament" x="390" y="966" width="420" height="68" rx="34" role="img" aria-label="Gold scrollwork flourish"/>
</svg>
</body>
</html>
```